Maple Hollow Bloom Panels Business card

Looking to have a business card design incorporating my logo for my flower wall business.

Industry/Entity Type

Wedding & event planning

Contact Information for Business Card

My business logo, my name - Lena Whitcombe (owner), my tagline - Let our blooms frame your moment, phone # 401-726-3148, email address - maplehollowbloompanels@mailvane.net, my website - maplehollowbloompanels.net, Instagram handle- @maplehollowbloompanels, FB handle Handle - maplehollowbloompanels

Font styles to use
Other font styles liked:
• Sentaina is the font that is used in my logo

Requirements
Must have
• Would like a double sided business card

```html
<!DOCTYPE html>
<html lang="en">
<head>
<meta charset="utf-8">
<title>Maple Hollow Bloom Panels – Business Card</title>
<link href="https://fonts.googleapis.com/css2?family=Allura&family=Open+Sans:wght@400&display=swap" rel="stylesheet">
<style>
  :root {
    --page: #ffffff;
    --blush: #f9dde8;
    --blush-deep: #f3cfdd;
    --ink: #222222;
    --edge: #2a2a2a;
    --paper: #ffffff;
  }
  html, body {
    margin: 0;
    padding: 0;
    width: 1200px;
    height: 1000px;
    overflow: hidden;
    background: var(--page);
  }
  .canvas {
    position: relative;
    width: 1200px;
    height: 1000px;
  }
  .card {
    position: absolute;
    left: 209px;
    width: 781px;
    height: 446px;
    box-sizing: border-box;
    border: 1px solid var(--edge);
    background: var(--blush);
    overflow: hidden;
  }
  .card--front { top: 40px; }
  .card--back { top: 514px; }

  .front-seal {
    position: absolute;
    left: 262px;
    top: 99px;
    width: 256px;
    height: 256px;
    border-radius: 50%;
    background: var(--paper);
    display: flex;
    align-items: center;
    justify-content: center;
    text-align: center;
  }
  .brand-name {
    font-family: "Allura", cursive;
    color: var(--ink);
    font-weight: 400;
    margin: 0;
    line-height: 1;
  }
  .front-seal .brand-name {
    font-size: 42px;
    line-height: 1.05;
  }

  .pattern-panel {
    position: absolute;
    top: 0;
    width: 173px;
    height: 100%;
    background: linear-gradient(180deg, var(--blush) 0%, var(--blush-deep) 50%, var(--blush) 100%);
  }
  .pattern-panel--left { left: 0; }
  .pattern-panel--right { right: 0; }

  .info-panel {
    position: absolute;
    left: 173px;
    top: 0;
    width: 435px;
    height: 100%;
    background: var(--paper);
    text-align: center;
  }
  .info-panel .brand-name {
    position: absolute;
    left: 0;
    right: 0;
    top: 48px;
    font-size: 40px;
  }
  .owner-name {
    position: absolute;
    left: 0;
    right: 0;
    top: 156px;
    margin: 0;
    font-family: "Allura", cursive;
    font-size: 32px;
    color: var(--ink);
    font-weight: 400;
  }
  .contact-list {
    position: absolute;
    left: 0;
    right: 0;
    top: 222px;
    margin: 0;
    padding: 0;
    list-style: none;
    font-family: "Open Sans", sans-serif;
    font-size: 15.5px;
    line-height: 22.5px;
    color: var(--ink);
    white-space: nowrap;
  }
  .tagline {
    position: absolute;
    left: 0;
    right: 0;
    top: 368px;
    margin: 0;
    font-family: "Allura", cursive;
    font-size: 28px;
    color: var(--ink);
    display: flex;
    align-items: center;
    justify-content: center;
    gap: 12px;
  }
  .tagline-dot {
    width: 6px;
    height: 6px;
    border-radius: 50%;
    background: var(--ink);
  }
</style>
</head>
<body>
<main class="canvas">

  <section class="card card--front" aria-label="Business card front">
    <div class="front-seal">
      <p class="brand-name">Maple Hollow<br>Bloom Panels</p>
    </div>
  </section>

  <section class="card card--back" aria-label="Business card back">
    <div class="pattern-panel pattern-panel--left" role="img" aria-label="Repeating pattern of pink line-drawn peony blossoms"></div>

    <div class="info-panel">
      <p class="brand-name">Maple Hollow Bloom Panels</p>
      <p class="owner-name">Lena Whitcombe</p>
      <ul class="contact-list">
        <li>Phone Number - 401-726-3148</li>
        <li>Email address - maplehollowbloompanels@mailvane.net</li>
        <li>Website - maplehollowbloompanels.net</li>
        <li>Instagram handle- @maplehollowbloompanels</li>
        <li>FB handle - maplehollowbloompanels</li>
      </ul>
      <p class="tagline"><span class="tagline-dot"></span>Let our blooms frame your moment<span class="tagline-dot"></span></p>
    </div>

    <div class="pattern-panel pattern-panel--right" role="img" aria-label="Repeating pattern of pink line-drawn peony blossoms"></div>
  </section>

</main>
</body>
</html>
```